Law Firm Stationery Design - Traditional Meets Intuitive

Looking for a modern, yet classic, law firm stationery design. Simplicity is desired, but great ideas are encouraged. See attachment for company information. We utilize a variety of non-traditional legal tools to bring a different perspective to each of our client's particular situation. Final design should communicate classic values with intuitive, unique solutions.

Industry/Entity Type

Law Firm

Requirements
Should not have
• - No typical legal icons
• - No Tag Line!
• - DO NOT WANT WHAT WE ALREADY HAVE

```html
<!DOCTYPE html>
<html lang="en">
<head>
<meta charset="utf-8">
<title>Meridian Law Stationery</title>
<link href="https://fonts.googleapis.com/css2?family=Libre+Baskerville&family=Source+Sans+3:wght@400;600;700&display=swap" rel="stylesheet">
<style>
:root{
  --board:#484848;
  --paper:#f5f4f2;
  --brand-blue:#0a64a4;
  --ink:#1a1a1a;
  --text:#555;
  --rule:#9a9a9a;
  --sans:"Source Sans 3",Arial,sans-serif;
  --serif:"Libre Baskerville",Georgia,serif;
}
*{margin:0;padding:0;box-sizing:border-box}
html,body{width:1200px;height:924px;overflow:hidden;background:var(--board)}
.board{position:relative;width:1200px;height:924px;font-family:var(--sans);color:var(--text)}
.sheet{position:absolute;background:var(--paper);box-shadow:0 4px 14px rgba(0,0,0,.35)}
.accent{position:absolute;background:var(--brand-blue)}
.wordmark{position:absolute;font-family:var(--serif);color:var(--ink);white-space:nowrap;line-height:1}
.abs{position:absolute}
.contact-list{list-style:none}
.contact-list li{display:flex;align-items:center;gap:5px}
.contact-list svg{flex:none}
.address{font-family:var(--sans)}
.address strong{font-weight:700;color:#444}

/* letterhead */
.letterhead{left:71px;top:78px;width:557px;height:787px}
.letterhead .wordmark{left:41px;top:69px;font-size:29px}
.salutation{left:41px;top:219px;font-size:15px;color:#555}
.letter-body{left:41px;top:268px;width:476px;font-size:8.5px;line-height:13.4px;color:#555}
.letter-body p{margin-bottom:13.4px}
.closing{left:41px;top:548px;font-size:8.6px;color:#555}
.signature{left:56px;top:566px;width:72px;height:28px;background:linear-gradient(90deg,#e8e7e5,#dedcda);border-radius:3px}
.signer{left:60px;top:608px;font-size:9.6px;line-height:14.5px;color:#555}
.letterhead .contact-list{left:41px;top:716px;font-size:8.8px;line-height:13.4px;color:#555}
.letterhead .address{right:51px;top:716px;text-align:right;font-size:8.4px;line-height:13.4px;color:#555}

/* envelope */
.envelope{left:499px;top:491px;width:628px;height:285px}
.envelope .wordmark{left:44px;top:45px;font-size:29px}
.envelope .address{left:46px;top:91px;font-size:10px;line-height:13px;color:#555}

/* business card front */
.card-front{left:677px;top:132px;width:245px;height:140px}
.card-front .wordmark{right:14px;top:32px;font-size:15px}
.holder{left:16px;top:73px}
.holder-name{font-size:9px;font-weight:700;color:var(--ink);line-height:10px}
.holder-role{font-size:6.8px;color:var(--brand-blue);line-height:9px}
.card-rule{left:16px;right:14px;top:94px;height:1px;background:var(--rule)}
.card-front .contact-list{left:16px;top:100px;font-size:6.6px;line-height:9px;color:#555}
.card-front .address{right:14px;top:101px;text-align:right;font-size:6.3px;line-height:9px;color:#555}

/* business card back */
.card-back{left:680px;top:313px;width:245px;height:139px;background:var(--brand-blue)}
.card-back .wordmark{right:9px;top:112px;font-size:15px;color:#fff}
</style>
</head>
<body>
<main class="board">

  <article class="sheet letterhead">
    <span class="accent" style="left:0;top:60px;width:10px;height:44px"></span>
    <div class="wordmark">Meridian Law</div>

    <p class="abs salutation">Dear Mr. Reyes,</p>
    <div class="abs letter-body">
      <p>Lorem ipsum dolor sit amet, consectetur adipiscing elit. Donec orci purus, luctus vitae dignissim eu, iaculis sed purus. Vivamus faucibus, ipsum nec aliquet viverra, leo mauris condimentum ligula, sit amet sagittis enim ligula quis arcu. Nam egestas tortor id nisi porttitor mattis. In tortor ante, ultricies in suscipit a, tempus non massa. Vivamus et auctor mi. Fusce vel massa nulla. Phasellus nec eros mauris, et scelerisque orci.</p>
      <p>Donec malesuada orci vitae nulla accumsan porta a id massa. Quisque accumsan iaculis magna sit amet fringilla. Maecenas consequat, magna eget tincidunt semper, odio nibh rutrum mi, id feugiat ante nisi eu risus. Vestibulum nunc orci, rhoncus a placerat in, ultricies in mi. Cras mattis varius eros, vel fringilla nisi suscipit eget. Quisque scelerisque sagittis nulla at porttitor.</p>
      <p>Sed id augue vitae urna euismod commodo aliquet a quam. Pellentesque arcu velit, cursus et malesuada ut, consequat et diam. Nullam erat sem, rhoncus id ullamcorper vitae, rhoncus et arcu. In ultricies ultricies nulla, ut dapibus elit. Donec eu magna a metus ornare faucibus. Fusce aliquet faucibus ultricies. Morbi semper, est id tincidunt adipiscing lacus, ac bibendum nulla leo eu purus. Quisque nec diam sed risus consectetur a accumsan vestibulum id purus lorem.</p>
      <p>It is a long established fact that a reader will be distracted by the readable content of a page when looking at its layout. The point of using Lorem Ipsum is that it has a more-or-less normal distribution of letters, as opposed to using 'Content here, content here', making it look like readable English. Many desktop publishing packages</p>
    </div>
    <p class="abs closing">Sincerely,</p>
    <div class="abs signature" role="img" aria-label="Handwritten signature of Daniel Reyes"></div>
    <p class="abs signer">Daniel Reyes<br>CEO/ Founder</p>

    <ul class="abs contact-list">
      <li><svg width="8" height="9" viewBox="0 0 8 10"><rect x="1.5" y=".5" width="5" height="9" rx="1" fill="none" stroke="#222"/><rect x="2.5" y="1.8" width="3" height="5.5" fill="#222"/></svg>555-014-2290</li>
      <li><svg width="8" height="9" viewBox="0 0 10 8"><rect x=".5" y="1" width="9" height="6" fill="#222"/><path d="M.5 1 5 4.5 9.5 1" fill="none" stroke="#f5f4f2" stroke-width=".8"/></svg>info@meridianlaw.com</li>
      <li><svg width="8" height="9" viewBox="0 0 10 10"><circle cx="5" cy="5" r="4.5" fill="#222"/><path d="M3 2.5c1.5.5 1 2 2.5 2.3M6 6.5c-.8.8-.3 1.8-1 2.5" stroke="#f5f4f2" stroke-width=".9" fill="none"/></svg>www.meridianlaw.com</li>
    </ul>
    <p class="abs address"><strong>MERIDIAN LAW LLC</strong><br>18 Harbor Lane, Suite 300<br>Easton, MA 02375</p>
  </article>

  <article class="sheet card-front">
    <div class="wordmark">Meridian Law</div>
    <span class="accent" style="left:0;top:74px;width:4px;height:17px"></span>
    <div class="abs holder">
      <p class="holder-name">DANIEL REYES</p>
      <p class="holder-role">CEO/Founder</p>
    </div>
    <span class="abs card-rule"></span>
    <ul class="abs contact-list">
      <li><svg width="6" height="7" viewBox="0 0 8 10"><rect x="1.5" y=".5" width="5" height="9" rx="1" fill="none" stroke="#222"/><rect x="2.5" y="1.8" width="3" height="5.5" fill="#222"/></svg>555-014-2290</li>
      <li><svg width="6" height="7" viewBox="0 0 10 8"><rect x=".5" y="1" width="9" height="6" fill="#222"/><path d="M.5 1 5 4.5 9.5 1" fill="none" stroke="#f5f4f2" stroke-width=".8"/></svg>info@meridianlaw.com</li>
      <li><svg width="6" height="7" viewBox="0 0 10 10"><circle cx="5" cy="5" r="4.5" fill="#222"/><path d="M3 2.5c1.5.5 1 2 2.5 2.3M6 6.5c-.8.8-.3 1.8-1 2.5" stroke="#f5f4f2" stroke-width=".9" fill="none"/></svg>www.meridianlaw.com</li>
    </ul>
    <p class="abs address"><strong>MERIDIAN LAW LLC</strong><br>18 Harbor Lane, Suite 300<br>Easton, MA 02375</p>
  </article>

  <article class="sheet card-back">
    <div class="wordmark">Meridian Law</div>
  </article>

  <article class="sheet envelope">
    <span class="accent" style="left:0;top:37px;width:12px;height:46px"></span>
    <div class="wordmark">Meridian Law</div>
    <p class="abs address"><strong>MERIDIAN LAW LLC</strong><br>18 Harbor Lane, Suite 300<br>Easton, MA 02375</p>
  </article>

</main>
</body>
</html>
```